Web-page design

We need a initial web design for our page kelbrook.com.au (which is not yet set up).
We provide consulting services for all kinds of problems in and between organisations.
Main focus is on conflict resolution but we also support companies on improving their operational performance.
We want to have the following page structure (and part of the project is to design the 8 pages):
- Home
- Services (we offer 3 main service areas - one per page)
- Case studies (one per page)
- Engaging us (our process)
- About Conflict & low performance
- Conflict resolution App
- About
- Contact (Email form)
- Our logo should be on each page.
The start page should include the following information:
- Twitter / Linkedin / facebook/ google + Links
- Telephone / Email or in general contact details
- News
- A quite prominent picture box with 3 alternating pics - each representing one of our service areas
- Link to our App
- Testimonials
It would be nice if the service pages would have an image header. Links to the information section (about conflict & low performance; and the app page) would be nice as well.
We like the following joomla designs: www.frandelthemes.com/itempreview/153
No need to copy it, it should just give you an idea.
We like the layout here with the picture and space for the case studies on the left. Somewhere beneath should be the 3 service areas with a picture each.
In terms of colors: our logo colours are Blue (RBG 8;44;80) and Orange (RGB 231;120;23). The orange could be used to emphasise certain things, however there should not be too much color.
Budget for images available, so please use placeholders or ask us for specific photos/images, if you need them for your design.
Updates
Hi, one more thing that we would like to have is the case studies not hidden behind a link "case studies" - we would like to have them individually linked prominent on the first page. There will be about 6-8 of them. Thats what we liked on the joomla template (the links left from the picture).
Hi, thanks very much for all the great proposals.
We are currently going through the selection process and will post our decision early next week.
Thanks again!
Wilma
Target Market(s)
- target customers are all different kinds of businesses and organisations (all industries, government, non-for-profit, ...) experiencing conflict and tension - be it with internal staff, amongst managers or board members, dysfunctional teams, between organizations or customers and organizations... examples could be bullying allegations, governmental negotiations with unions, disputes within organizations etc.
- also we will offer performance improvement services for organizations
- we will offer mediation, facilitation, negotiation, performance improvement services, conflict coaching, conflict management, change management services
- if comparable to anything - then to a law firm in terms of dealing with conflicts but its much less adversarial and much more about the people and their interests rather than about laws
- basically it's all kind of things you can do in order to solve disputes without involving lawyers and a court - so it's much cheaper and target is to find a solution all parties can live with rather than having a judge deciding about who wins and who looses
- performance management is more about analysing reasons for a lack of performance and setting up continous improvement systems, supporting change management, facilitating improvement workshops or strategic meetings, ...
Industry/Entity Type
Consulting
Look and feel

```html
<!DOCTYPE html>
<html lang="en">
<head>
<meta charset="utf-8">
<title>Kelbrook Hale – Conflict Resolution &amp; Performance Consulting</title>
<link rel="stylesheet" href="https://fonts.googleapis.com/css2?family=Oswald:wght@400;500;600&family=Open+Sans:wght@400;600&display=swap">
<style>
:root{
  --navy:#082c50;
  --orange:#f0832e;
  --orange-deep:#e77817;
  --dark:#262626;
  --darker:#1c1c1c;
  --bar:#2b2b2b;
  --light:#f2f2f2;
  --grey-text:#9a9a9a;
  --body-light:#d2d2d2;
  --field:#4a4a4a;
}
*{box-sizing:border-box;margin:0;padding:0}
html,body{width:892px;height:1200px;overflow:hidden;background:#fff}
body{font-family:"Open Sans",Arial,sans-serif;color:#333}
.page{position:relative;width:892px;height:1200px;overflow:hidden}
.abs{position:absolute}
.cond{font-family:"Oswald","Arial Narrow",sans-serif}

/* top bar */
.topbar{left:0;top:0;width:892px;height:22px;background:var(--light)}
.topbar .contact-line{left:62px;top:5px;font-size:7.5px;color:#888;white-space:nowrap}
.topbar .social{left:728px;top:5px;display:flex;gap:9px}
.dot{width:10px;height:10px;border-radius:50%;background:#9aa3ab}
.dot.active{background:var(--navy)}
.search-box{left:806px;top:0;width:24px;height:22px;background:#fff}

/* header */
.brand{left:0;top:22px;width:892px;height:79px;text-align:center}
.brand-name{position:absolute;left:0;right:0;top:24px;display:flex;justify-content:center;align-items:center;gap:9px;font-size:21px;color:var(--navy);letter-spacing:.5px}
.brand-mark{width:16px;height:16px;background:var(--orange-deep)}
.brand-url{position:absolute;left:0;right:0;top:55px;font-size:8.5px;letter-spacing:5.5px;color:var(--navy)}

/* nav */
.nav{left:0;top:101px;width:892px;height:37px;background:var(--bar);border-bottom:2px solid var(--orange)}
.nav-home{left:90px;top:0;width:52px;height:35px;background:var(--orange);display:flex;align-items:center;justify-content:center}
.nav-home span{width:14px;height:14px;border:2px solid #fff}
.nav ul{position:absolute;left:146px;top:9px;display:flex;list-style:none;font-size:12.5px;color:#fff;white-space:nowrap}
.nav li{padding:0 10px;border-left:1px solid #555;line-height:17px;letter-spacing:-.2px}
.nav li:first-child{border-left:none}

/* hero */
.hero{left:0;top:138px;width:892px;height:244px;background:linear-gradient(100deg,#cfe2f1 0%,#e8eff4 35%,#f4f1ec 55%,#d8cfc7 75%,#b3a197 100%)}
.hero-photo{left:330px;top:0;width:260px;height:244px;background:radial-gradient(ellipse at 50% 55%,#f3f3f3 0%,#dfe3e8 45%,rgba(220,226,232,0) 75%)}
.cases{left:93px;top:22px;width:174px;background:rgba(240,240,240,.92)}
.cases h2{height:33px;background:var(--navy);color:#fff;font-size:15px;font-weight:500;padding:6px 0 0 20px;letter-spacing:.3px}
.cases ul{list-style:none;padding:2px 0 6px}
.cases li{height:20.5px;font-size:9.5px;color:#444;padding:4px 0 0 32px;border-bottom:1px solid #dcdcdc;position:relative;letter-spacing:.3px}
.cases li::before{content:"";position:absolute;left:22px;top:8px;border:2.5px solid transparent;border-left:3px solid #aaa}
.cases li.current{background:var(--orange);color:#fff}
.cases li.current::before{border-left-color:#fff}
.hero-title{left:580px;top:66px;font-size:30px;color:var(--navy);letter-spacing:-.3px;font-weight:500}
.hero-points{left:580px;top:106px;list-style:none}
.hero-points li{display:flex;align-items:center;height:22px;font-size:10px;color:#555}
.hero-points i{width:16px;height:16px;border:2px solid var(--orange);border-radius:50%;margin-right:13px;display:inline-block}
.arrow-btn{width:22px;height:22px;border-radius:50%;background:rgba(255,255,255,.75);color:#666;font-size:12px;display:flex;align-items:center;justify-content:center}
.slider-dots{left:792px;top:224px;display:flex;gap:5px}
.slider-dots span{width:9px;height:9px;border-radius:50%;border:2px solid #fff}
.slider-dots span.on{border-color:var(--orange)}

/* services */
.services{left:0;top:382px;width:892px;height:242px;background:var(--dark)}
.service{top:38px;width:220px;text-align:center}
.service-head{display:flex;align-items:center;justify-content:center;gap:13px}
.service-icon{width:39px;height:39px;border-radius:50%;background:#fff;display:flex;align-items:center;justify-content:center}
.service h3{font-size:28px;color:var(--orange);font-weight:400;letter-spacing:-.3px}
.service p{margin-top:12px;font-size:11.6px;line-height:15.2px;color:var(--body-light)}
.btn{display:inline-block;border-radius:16px;background:#333;color:#fff;border:2px solid #1a1a1a;box-shadow:0 0 0 1px #444}
.service .btn{margin-top:20px;width:94px;height:32px;font-size:15px;line-height:28px}

/* welcome */
.welcome{left:0;top:624px;width:892px;height:279px;background:var(--orange)}
.welcome h2{left:100px;top:48px;font-size:21px;color:#1e1e1e;font-weight:600}
.welcome .intro{left:100px;top:82px;width:320px;font-size:11.3px;line-height:16.6px;color:#1e1e1e}
.welcome .intro p+p{margin-top:16px}
.divider{left:446px;top:59px;width:1px;height:175px;background:#d46a1d}
.client-label{left:473px;top:55px;font-size:14px;color:#1e1e1e;font-weight:500}
.client-photo{left:473px;top:83px;width:66px;height:67px;border:3px solid #fff;background:linear-gradient(160deg,#d9c9bd,#9c8272 60%,#5a5048)}
.quote{left:567px;top:58px;width:225px;height:166px;background:var(--dark);padding:17px 16px 0 21px}
.quote::before{content:"";position:absolute;left:-19px;top:22px;border-top:12px solid transparent;border-right:19px solid var(--dark);border-bottom:0 solid transparent}
.quote h4{font-size:16px;color:#fff;font-weight:400}
.quote p{margin-top:9px;font-size:9.3px;line-height:15.2px;color:#ddd}
.quote .pager{position:absolute;right:15px;top:8px;color:#ccc;font-size:12px;letter-spacing:4px}

/* footer */
.footer{left:0;top:903px;width:892px;height:252px;background:#252525}
.footer h3{position:absolute;top:30px;font-size:17px;color:#fff;font-weight:400;letter-spacing:-.2px}
.footer h3::after{content:"";position:absolute;left:0;top:30px;width:52px;height:2px;background:var(--orange)}
.quick-links{left:104px;top:66px;list-style:none}
.quick-links li{height:22px;font-size:9.8px;color:var(--grey-text);padding-left:17px;position:relative;letter-spacing:.2px}
.quick-links li::before{content:"";position:absolute;left:0;top:3px;border:2.5px solid transparent;border-left:3px solid #bbb}
.about-text{left:356px;top:67px;width:190px;font-size:9.8px;line-height:13.6px;color:var(--grey-text)}
.about-text p+p{margin-top:12px}
.footer .btn{position:absolute;height:24px;font-size:10.5px;line-height:20px;text-align:center;border-radius:13px}
.field{position:absolute;left:604px;width:188px;background:var(--field);font-size:10px;color:#aaa;padding:6px 10px}
.to-top{left:832px;top:191px;width:31px;height:31px;background:#1c1c1c}
.bottombar{left:0;top:1155px;width:892px;height:45px;background:var(--darker)}
.bottombar .mark{left:102px;top:14px;width:15px;height:15px;border:2px solid #aaa}
.bottombar .copy{left:127px;top:16px;font-size:10px;color:#bbb}
.bottombar .social{left:706px;top:17px;display:flex;gap:12px}
.bottombar .social span{width:12px;height:12px;border-radius:50%;background:#9a9a9a}
</style>
</head>
<body>
<div class="page">

  <div class="abs topbar">
    <div class="abs contact-line">&#9742; +1 800 555-0142 &nbsp; &#9993; contact@kelbrook.com.au</div>
    <div class="abs social" aria-label="Social network links">
      <span class="dot active"></span><span class="dot"></span><span class="dot"></span><span class="dot"></span>
    </div>
    <div class="abs search-box">
      <svg width="24" height="22" viewBox="0 0 24 22"><circle cx="11" cy="10" r="3.5" fill="none" stroke="#f0832e" stroke-width="1.6"/><line x1="13.5" y1="12.5" x2="16" y2="15" stroke="#f0832e" stroke-width="1.8"/></svg>
    </div>
  </div>

  <header class="abs brand">
    <div class="brand-name"><span>KELBROOK HALE</span><span class="brand-mark"></span></div>
    <div class="brand-url">www.kelbrook.com.au</div>
  </header>

  <nav class="abs nav cond">
    <div class="abs nav-home"><span></span></div>
    <ul>
      <li>SERVICES &#9662;</li>
      <li>CASE STUDIES &#9662;</li>
      <li>ENGAGING US</li>
      <li>ABOUT CONFLICT &amp; LOW PERFORMANCE</li>
      <li>CONFLICT RESOLUTION APP</li>
      <li>ABOUT</li>
      <li>CONTACT</li>
    </ul>
  </nav>

  <section class="abs hero">
    <div class="abs hero-photo" role="img" aria-label="Photo of a businessman with arms spread wide against a soft sky"></div>
    <aside class="abs cases">
      <h2 class="cond">CASE STUDIES</h2>
      <ul>
        <li>Managing Services</li>
        <li>Consulting Services</li>
        <li class="current">Policy Analysis</li>
        <li>Market Assessment</li>
        <li>Program Management</li>
        <li>Regulatory Support</li>
        <li>Risk Assessment</li>
        <li>Market Research</li>
      </ul>
    </aside>
    <h1 class="abs hero-title cond">LOREM IPSUM DOLOR</h1>
    <ul class="abs hero-points">
      <li><i></i>Sed ut eros ac diam dapibus commodo</li>
      <li><i></i>Sed ut eros ac diam dapibus</li>
      <li><i></i>Sed ut eros ac diam</li>
    </ul>
    <div class="abs arrow-btn" style="left:14px;top:114px">&#8249;</div>
    <div class="abs arrow-btn" style="left:846px;top:114px;color:var(--orange)">&#8250;</div>
    <div class="abs slider-dots"><span class="on"></span><span></span><span></span></div>
  </section>

  <section class="abs services">
    <div class="abs service" style="left:88px">
      <div class="service-head">
        <div class="service-icon">
          <svg width="22" height="22" viewBox="0 0 22 22"><circle cx="11" cy="9" r="5" fill="none" stroke="#f0832e" stroke-width="1.5"/><rect x="8.5" y="14" width="5" height="4" fill="#f0832e"/></svg>
        </div>
        <h3 class="cond">ACCESS</h3>
      </div>
      <p>Aute iure reprehenderit in voluptate velit esse cillum dolore eu fugiat nulla pariatur. Lorem ipsum dolor sit amet, consetetur sadipscing elitr, sed diam.</p>
      <span class="btn cond">KNOW MORE</span>
    </div>
    <div class="abs service" style="left:336px">
      <div class="service-head">
        <div class="service-icon">
          <svg width="26" height="22" viewBox="0 0 26 22"><circle cx="9" cy="11" r="5" fill="none" stroke="#f0832e" stroke-width="3" stroke-dasharray="2.5 1.5"/><circle cx="19" cy="11" r="3.5" fill="none" stroke="#f0832e" stroke-width="2.5" stroke-dasharray="2 1.4"/></svg>
        </div>
        <h3 class="cond">RESOLVE</h3>
      </div>
      <p>Aute iure reprehenderit in voluptate velit esse cillum dolore eu fugiat nulla pariatur. Lorem ipsum dolor sit amet, consetetur sadipscing elitr, sed diam.</p>
      <span class="btn cond">KNOW MORE</span>
    </div>
    <div class="abs service" style="left:585px">
      <div class="service-head">
        <div class="service-icon">
          <svg width="22" height="22" viewBox="0 0 22 22"><rect x="3" y="14" width="3" height="5" fill="#f0832e"/><rect x="8" y="11" width="3" height="8" fill="#f0832e"/><rect x="13" y="8" width="3" height="11" fill="#f0832e"/><polyline points="3,10 9,6 13,7 19,2" fill="none" stroke="#f0832e" stroke-width="1.5"/></svg>
        </div>
        <h3 class="cond">DEVELOP</h3>
      </div>
      <p>Aute iure reprehenderit in voluptate velit esse cillum dolore eu fugiat nulla pariatur. Lorem ipsum dolor sit amet, consetetur sadipscing elitr, sed diam.</p>
      <span class="btn cond">KNOW MORE</span>
    </div>
  </section>

  <section class="abs welcome">
    <h2 class="abs cond">WELCOME</h2>
    <div class="abs intro">
      <p>orem ipsum dolor sit amet, consectetur adipiscursus felis vel lacus cursus ullamcorper. Maecenas sed enim neque, quis rutrum arcu. Meceasa justo enim. Suspendisse suscipit malesuada magna, at sagittis augue varius ut.</p>
      <p>orem ipsum dolor sit amet, consectetur adipiscursus felis vel lacus cursus ullamcorper. Maecenas sed enim neque, quis rutrum arcu. Meceasa justo enim. Suspendisse suscipit.</p>
    </div>
    <div class="abs divider"></div>
    <div class="abs client-label cond">CLIENT SAYS</div>
    <div class="abs client-photo" role="img" aria-label="Portrait photo of the client giving the testimonial"></div>
    <blockquote class="abs quote">
      <span class="pager">&#8249;&#8250;</span>
      <h4 class="cond">- Owen Hartley</h4>
      <p>orem ipsum dolor sit amet, consectetur adipiscursus felis vel lacus cursus ullamcorper. Maecenas sed enim neque, quis rutrum arcu. Meceasa justo enim. Suspendisse suscipit malesuada magna, at sagittis augue varius ut.</p>
    </blockquote>
  </section>

  <footer class="abs footer">
    <h3 class="cond" style="left:104px">QUICK LINK</h3>
    <ul class="abs quick-links">
      <li>Services</li>
      <li>Case Studies</li>
      <li>Engaging Us</li>
      <li>About Conflict &amp; Low Performance</li>
      <li>Conflict Resolution App</li>
      <li>About</li>
      <li>Contact</li>
    </ul>

    <h3 class="cond" style="left:359px">ABOUT US</h3>
    <div class="abs about-text">
      <p>Aute iure reprehenderit in voluptate velit esse cillum dolore eu fugiat nulla pariatur. Lorem ipsum dolor sit amet, consetetur sadipscing elitr, sed diam.</p>
      <p>Aute iure reprehenderit in voluptate velit esse cillum dolore eu fugiat nulla pariatur. Lorem ipsum dolor sit amet, consetetur sadipscing.</p>
    </div>
    <span class="btn cond" style="left:356px;top:198px;width:71px">READ MORE</span>

    <h3 class="cond" style="left:604px">CONTACT FORM</h3>
    <div class="field" style="top:72px;height:24px">Your Name:*</div>
    <div class="field" style="top:104px;height:24px">Your Email:*</div>
    <div class="field" style="top:136px;height:52px">Your Message:*</div>
    <span class="btn cond" style="left:717px;top:198px;width:75px">SEND MESSAGE</span>

    <div class="abs to-top">
      <svg width="31" height="31" viewBox="0 0 31 31"><polyline points="10,18 15.5,12.5 21,18" fill="none" stroke="#bbb" stroke-width="1.6"/></svg>
    </div>
  </footer>

  <div class="abs bottombar">
    <span class="abs mark"></span>
    <span class="abs copy">Copyright &copy; 2013 &nbsp;All Rights Reserved.</span>
    <div class="abs social" aria-label="Social network links"><span></span><span></span><span></span><span></span></div>
  </div>

</div>
</body>
</html>
```